Ridgeline Wild Craft DL flyer

I'm looking for a new flyer for my startup business. In Darwin Australia.
Aimed at family's and short stay tourists the "Ridgeline Wild Craft" 4 hr tour will give people a basic understanding of some essential bush survival skills in the Australian Outback.
things covered in this 4 hr tour are
1. Finding water.
2. finding food.
3. Finding/making shelter and fire.
4. Finding your way home.

The tour will pick clients up in an air conditioned purpose build 4WD and take them to a nearby bushland area where they will have the opportunity to catch and harvest some native bushtucker.
They will then be able to find/harvest some water for survival situations.
While we cook our bush tucker they will also learn to find their way home through ancient navigation techniques as well.

Clients will then be dropped back to their accomodation with some fun and vital knowledge of surviving in the Australian outback.
At the end of the tour the group will be able to take home a basic survival kit which they will be able to use through the skills they just gained on the tour.

I'd like a two sided DL size flyer emphasising the following points.
4hr/half day tour
Fun for the family
Free survival kit included.
Eat what you catch
Learn essential survival skills
Provided buy an experienced and passionate bushman.
$150/head including transfers.

I'll provide some pictures for the flyer and any extra content you require.

Target Market(s)

Family's
Short stay tourists

Industry/Entity Type

Tourism

Colors

Designer to choose colors to be used in the design.

Requirements
Must have
• As per brief
Nice to have
• Any extra content and flair designers would like to add
Should not have
• Any images which aren't Australian

```html
<!DOCTYPE html>
<html lang="en">
<head>
<meta charset="utf-8">
<title>Ridgeline Wild Craft – DL Flyer</title>
<link rel="stylesheet" href="https://fonts.googleapis.com/css2?family=Cinzel:wght@600;700&family=Cormorant+Garamond:wght@500;600&family=Share+Tech+Mono&family=PT+Sans+Narrow:wght@400;700&display=swap">
<style>
  :root {
    --page-bg: #e9e6e1;
    --paper-light: #f4ead0;
    --paper-mid: #ead9ae;
    --paper-dark: #d6bb82;
    --olive: #8e9633;
    --olive-dark: #6f7526;
    --ink: #1c1a14;
    --accent: #e8501f;
    --white: #ffffff;
    --photo-green-1: #5d7a3a;
    --photo-green-2: #2f4a24;
    --photo-skin: #b9785a;
    --photo-earth: #9a7a55;
    --photo-earth-dark: #5e4a36;
  }
  * { box-sizing: border-box; margin: 0; padding: 0; }
  html, body { width: 1126px; height: 1200px; overflow: hidden; }
  body { background: var(--page-bg); position: relative; font-family: "Cormorant Garamond", Georgia, serif; }

  .flyer {
    position: absolute;
    width: 474px;
    height: 992px;
    overflow: hidden;
    background: radial-gradient(ellipse at 40% 45%, var(--paper-light) 0%, var(--paper-mid) 60%, var(--paper-dark) 100%);
    box-shadow: 0 6px 18px rgba(0,0,0,.25);
  }
  .flyer--front { left: 62px; top: 58px; }
  .flyer--back  { left: 590px; top: 150px; }

  .hero { position: absolute; left: 0; top: 0; width: 100%; }
  .hero svg { display: block; }

  .inset-photo {
    position: absolute; border: 6px solid var(--white);
    box-shadow: 0 3px 8px rgba(0,0,0,.35);
  }
  .inset-photo--round {
    left: 18px; top: 288px; width: 166px; height: 166px; border-radius: 50%;
    background: radial-gradient(circle at 55% 50%, #8fae3c 0%, var(--photo-skin) 55%, #7a5a40 100%);
  }

  .brand { position: absolute; left: 22px; right: 22px; top: 395px; font-family: "Cinzel", "Times New Roman", serif; font-weight: 700; }
  .brand__top { text-align: right; color: var(--olive-dark); font-size: 44px; line-height: 1; letter-spacing: -1px; }
  .brand__bottom { font-size: 60px; line-height: 1.1; letter-spacing: -2px; color: var(--ink); white-space: nowrap; }
  .brand__bottom .olive { color: var(--olive-dark); }
  .brand__rule { height: 2px; background: var(--olive); margin-top: 6px; }

  .mono { font-family: "Share Tech Mono", "Courier New", monospace; color: var(--accent); letter-spacing: 2px; }
  .tagline { position: absolute; left: 0; right: 0; top: 572px; text-align: center; font-size: 20px; line-height: 1.45; }

  .checklist { position: absolute; left: 24px; top: 660px; list-style: none; }
  .checklist li { display: flex; align-items: center; gap: 12px; font-size: 22px; color: var(--ink); height: 37px; font-weight: 500; }
  .checklist svg { flex: none; }

  .tilt-photo { position: absolute; border: 7px solid var(--white); box-shadow: 2px 4px 10px rgba(0,0,0,.35); }
  .tilt-photo--mounds {
    left: 288px; top: 670px; width: 178px; height: 128px; transform: rotate(9deg);
    background: linear-gradient(180deg, #9fb9c8 0%, #7d9a52 40%, #a3562d 70%, #6f8a3a 100%);
  }

  .price { position: absolute; font-size: 17px; }
  .flyer--front .price { left: 0; right: 0; top: 855px; text-align: center; }

  .footer-band { position: absolute; left: 0; bottom: 0; width: 100%; height: 100px; }
  .footer-band svg { position: absolute; left: 0; top: 0; }
  .footer-band__text { position: absolute; left: 0; right: 0; top: 24px; text-align: center; color: var(--white); }
  .book-now { font-family: "PT Sans Narrow", Arial, sans-serif; font-size: 27px; letter-spacing: -.5px; line-height: 1.15; }
  .site { font-family: "Share Tech Mono", "Courier New", monospace; font-size: 20px; letter-spacing: 3px; margin-top: 6px; }

  /* back */
  .top-band { position: absolute; left: 0; top: 0; width: 100%; height: 56px; background: var(--olive); }
  .headline {
    position: absolute; left: 0; right: 0; top: 196px; text-align: center;
    font-family: "Cinzel", "Times New Roman", serif; font-weight: 700; color: var(--white);
    font-size: 48px; line-height: 1.25; letter-spacing: -1px;
    text-shadow: 0 2px 4px rgba(0,0,0,.45);
  }
  .intro { position: absolute; left: 18px; right: 18px; top: 382px; text-align: center; color: var(--accent); font-size: 21px; line-height: 1.45; font-weight: 500; }

  .topics { position: absolute; left: 24px; top: 560px; list-style: none; }
  .topics li { display: flex; gap: 8px; font-size: 23px; color: var(--ink); line-height: 1.4; margin-bottom: 10px; font-weight: 500; }
  .topics .num { color: var(--olive-dark); font-weight: 600; font-size: 27px; line-height: 1.2; }

  .tilt-photo--compass {
    left: 300px; top: 552px; width: 160px; height: 130px; transform: rotate(12deg);
    background: linear-gradient(160deg, #a98c63 0%, var(--photo-earth) 50%, #7d6446 100%);
  }
  .tilt-photo--guide {
    left: 272px; top: 700px; width: 184px; height: 146px; transform: rotate(-8deg);
    background: linear-gradient(180deg, #a9c2cf 0%, #7e8c6a 45%, #5e6a55 100%);
  }
  .flyer--back .price { left: 22px; top: 822px; text-align: center; line-height: 1.45; }
</style>
</head>
<body>

<!-- FRONT -->
<section class="flyer flyer--front">
  <div class="hero">
    <svg width="474" height="380" viewBox="0 0 474 380">
      <defs>
        <linearGradient id="front-hero-fill" x1="0" y1="0" x2="1" y2="1">
          <stop offset="0" stop-color="var(--photo-green-1)"/>
          <stop offset=".5" stop-color="var(--photo-skin)"/>
          <stop offset="1" stop-color="var(--photo-green-2)"/>
        </linearGradient>
      </defs>
      <path role="img" aria-label="Photo: bushman by a river holding up a large mud crab" d="M0 0H474V330C380 358 260 365 140 340 80 328 30 318 0 318Z" fill="url(#front-hero-fill)"/>
      <path d="M0 318C40 322 90 334 150 346 260 366 380 360 474 332V342C380 372 250 374 140 352 80 340 30 330 0 330Z" fill="var(--white)"/>
    </svg>
  </div>
  <div class="inset-photo inset-photo--round" role="img" aria-label="Photo: hand holding green native bush fruit"></div>

  <div class="brand">
    <div class="brand__top">RIDGELINE</div>
    <div class="brand__bottom">WILD <span class="olive">CRAFT</span></div>
    <div class="brand__rule"></div>
  </div>

  <p class="tagline mono">Provided buy an experienced and<br>passionate bushman.</p>

  <ul class="checklist">
    <li><svg width="22" height="20" viewBox="0 0 22 20"><rect x="1" y="3" width="16" height="16" fill="none" stroke="var(--olive-dark)" stroke-width="2"/><path d="M4 10l4 4L20 2" fill="none" stroke="var(--olive-dark)" stroke-width="2.4"/></svg>4hr/half day tour.</li>
    <li><svg width="22" height="20" viewBox="0 0 22 20"><rect x="1" y="3" width="16" height="16" fill="none" stroke="var(--olive-dark)" stroke-width="2"/><path d="M4 10l4 4L20 2" fill="none" stroke="var(--olive-dark)" stroke-width="2.4"/></svg>Free survival kit included.</li>
    <li><svg width="22" height="20" viewBox="0 0 22 20"><rect x="1" y="3" width="16" height="16" fill="none" stroke="var(--olive-dark)" stroke-width="2"/><path d="M4 10l4 4L20 2" fill="none" stroke="var(--olive-dark)" stroke-width="2.4"/></svg>Fun for the family!</li>
    <li><svg width="22" height="20" viewBox="0 0 22 20"><rect x="1" y="3" width="16" height="16" fill="none" stroke="var(--olive-dark)" stroke-width="2"/><path d="M4 10l4 4L20 2" fill="none" stroke="var(--olive-dark)" stroke-width="2.4"/></svg>Eat what you catch!</li>
    <li><svg width="22" height="20" viewBox="0 0 22 20"><rect x="1" y="3" width="16" height="16" fill="none" stroke="var(--olive-dark)" stroke-width="2"/><path d="M4 10l4 4L20 2" fill="none" stroke="var(--olive-dark)" stroke-width="2.4"/></svg>Learn essential survival skills!</li>
  </ul>
  <div class="tilt-photo tilt-photo--mounds" role="img" aria-label="Photo: termite mounds in outback grassland"></div>

  <p class="price mono">$150/head including transfers.</p>

  <div class="footer-band">
    <svg width="474" height="100" viewBox="0 0 474 100">
      <path d="M0 10L20 6 38 12 60 5 82 11 104 4 130 10 152 6 176 12 200 5 224 10 250 4 272 11 298 6 320 12 346 5 370 10 394 4 418 11 442 6 474 10V100H0Z" fill="var(--paper-light)" opacity=".8"/>
      <path d="M0 16L22 12 40 18 62 11 84 17 106 10 132 16 154 12 178 18 202 11 226 16 252 10 274 17 300 12 322 18 348 11 372 16 396 10 420 17 444 12 474 16V100H0Z" fill="var(--olive)"/>
    </svg>
    <div class="footer-band__text">
      <div class="book-now">BOOK NOW</div>
      <div class="site">www.RidgelineWildCraft.au</div>
    </div>
  </div>
</section>

<!-- BACK -->
<section class="flyer flyer--back">
  <div class="top-band"></div>
  <div class="hero" style="top:48px">
    <svg width="474" height="330" viewBox="0 0 474 330">
      <defs>
        <linearGradient id="back-hero-fill" x1="0" y1="0" x2="1" y2="1">
          <stop offset="0" stop-color="#c9a08c"/>
          <stop offset=".45" stop-color="#6f8a6a"/>
          <stop offset="1" stop-color="var(--photo-earth-dark)"/>
        </linearGradient>
      </defs>
      <path d="M0 4L24 0 50 6 78 1 104 7 132 2 160 8 190 2 220 7 250 1 280 6 310 2 340 8 370 2 400 7 430 1 474 5V300C380 324 270 326 160 304 90 292 40 284 0 282Z" fill="url(#back-hero-fill)" role="img" aria-label="Photo: hands holding a blue-clawed freshwater crayfish"/>
      <path d="M0 282C40 284 90 292 160 304 270 326 380 324 474 300V312C380 336 260 338 150 316 85 304 38 296 0 294Z" fill="var(--white)"/>
    </svg>
  </div>
  <h2 class="headline">EAT WHAT<br>YOU CATCH!</h2>

  <p class="intro">Aimed at family's and short stay tourists the "Ridgeline Wild Craft" 4 hr tour will give people a basic understanding of some essential bush survival skills in the Australian Outback. things covered in this 4 hr tour are</p>

  <ol class="topics">
    <li><span class="num">1.</span><span>Finding water</span></li>
    <li><span class="num">2.</span><span>Finding food</span></li>
    <li><span class="num">3.</span><span>Finding/making shelter<br>and fire.</span></li>
    <li><span class="num">4.</span><span>Finding your way<br>home</span></li>
  </ol>
  <div class="tilt-photo tilt-photo--compass" role="img" aria-label="Photo: sticks laid on dirt marking east and west"></div>
  <div class="tilt-photo tilt-photo--guide" role="img" aria-label="Photo: bush guide in a wide-brim hat outdoors"></div>

  <p class="price mono">$150/head including<br>transfers.</p>

  <div class="footer-band">
    <svg width="474" height="100" viewBox="0 0 474 100">
      <path d="M0 10L20 6 38 12 60 5 82 11 104 4 130 10 152 6 176 12 200 5 224 10 250 4 272 11 298 6 320 12 346 5 370 10 394 4 418 11 442 6 474 10V100H0Z" fill="var(--paper-light)" opacity=".8"/>
      <path d="M0 16L22 12 40 18 62 11 84 17 106 10 132 16 154 12 178 18 202 11 226 16 252 10 274 17 300 12 322 18 348 11 372 16 396 10 420 17 444 12 474 16V100H0Z" fill="var(--olive)"/>
    </svg>
    <div class="footer-band__text">
      <div class="book-now">BOOK NOW</div>
      <div class="site">www.RidgelineWildCraft.au</div>
    </div>
  </div>
</section>

</body>
</html>
```